Business Card Design Project

Business card incoporating newly designed logo. The business cards will be magnets and I would like the same design as previously provided (Blue colour swatch with logo up the top) Please note that the logo incorporates a website so it needs to be legible.
The blue colours in teh swatch ideally will be in the same range as the blue of the logo.
The copy should all be in the same colour ie. black if in the white lines or white if in the swatch itself
Updates

Hi All

Some of the designs are very close to what I am after.  I have added logo and updated brief to assist with design.  This project is not refundable so I will be selecting a design.

Hi All

We are looking for a business card as per the brief (colour swatch style) as mentioned it is also a magnet so it needs to be created to the specs supplied.  Being a magnet there is also no requirment for reverse design.

Cheers
Marcy

Industry/Entity Type

Business

Requirements
Must have
• Blue colour swatch design. (see attached current example)
KW Coatings logo (colour) up the top
I require 1 design but 2 versions (with two peoples names and mobile numbers)

The magnets will be printed by PrintHollow.com.au And you can find the full specs online http://www.printhollow.com.au/custom-magnets.aspx

```html
<!DOCTYPE html>
<html lang="en">
<head>
<meta charset="utf-8">
<title>KW Coatings – Business Card Magnets</title>
<link rel="stylesheet" href="https://fonts.googleapis.com/css2?family=Source+Sans+3:wght@400;500&display=swap">
<style>
  :root {
    --page: #ffffff;
    --card-edge: #8a8a8a;
    --cream: #f7f4e2;
    --sand: #efe2c2;
    --navy: #2b3d8c;
    --deep-navy: #2c3a7e;
    --royal: #2f4ea0;
    --sky: #7390c8;
    --ink: #111111;
    --paper-text: #ffffff;
  }
  * { margin: 0; padding: 0; box-sizing: border-box; }
  html, body {
    width: 1200px;
    height: 1086px;
    overflow: hidden;
    background: var(--page);
  }
  .sheet { position: relative; width: 1200px; height: 1086px; }
  .card {
    position: absolute;
    width: 844px;
    height: 486px;
    border: 1px solid var(--card-edge);
    overflow: hidden;
  }
  .card--kevin { left: 72px; top: 64px; }
  .card--owen { left: 262px; top: 566px; }
  .card svg { display: block; width: 100%; height: 100%; }
  .card text { font-family: "Source Sans 3", sans-serif; }
  .bg-cream { fill: var(--cream); }
  .bg-sand { fill: var(--sand); }
  .band-navy { fill: var(--navy); }
  .band-deep { fill: var(--deep-navy); }
  .band-royal { fill: var(--royal); }
  .band-sky { fill: var(--sky); }
  .brand { font-size: 17px; fill: var(--ink); }
  .holder { font-size: 12px; fill: var(--ink); }
  .phone { font-size: 13px; fill: var(--ink); }
  .service { font-size: 12px; fill: var(--paper-text); }
  .contact { font-size: 13px; fill: var(--paper-text); }
</style>
</head>
<body>
<main class="sheet">

  <article class="card card--kevin">
    <svg viewBox="0 0 422 243" preserveAspectRatio="none">
      <rect class="bg-cream" width="422" height="243"/>
      <rect class="bg-sand" width="422" height="54"/>
      <polygon class="band-navy" points="0,51 422,57 422,86 0,82"/>
      <polygon class="band-royal" points="0,104 422,98 422,128 0,132"/>
      <polygon class="band-royal" points="0,141 422,150 422,185 0,178"/>
      <rect class="band-sky" x="0" y="192" width="422" height="29"/>
      <text class="brand" x="21" y="20">KW Coatings</text>
      <text class="brand" x="21" y="44">Kevin Walsh</text>
      <text class="holder" x="21" y="97">Kevin Walsh</text>
      <text class="phone" x="415" y="144" text-anchor="end">Phone Number:&#160; 0400 555 018</text>
      <text class="service" x="21" y="166">Commercial &amp; Domestic Painting</text>
      <text class="contact" x="21" y="212">Contact Us: KevinWalshCoatings@inbox.com.au</text>
    </svg>
  </article>

  <article class="card card--owen">
    <svg viewBox="0 0 422 243" preserveAspectRatio="none">
      <rect class="bg-cream" width="422" height="243"/>
      <polygon class="band-sky" points="0,50 422,55 422,85 0,80"/>
      <polygon class="band-royal" points="0,104 422,96 422,129 0,133"/>
      <polygon class="band-royal" points="0,141 422,148 422,185 0,178"/>
      <rect class="band-deep" x="0" y="193" width="422" height="28"/>
      <rect class="bg-sand" x="0" y="221" width="422" height="22"/>
      <text class="brand" x="21" y="20">KW Coatings</text>
      <text class="brand" x="21" y="44">Kevin Walsh</text>
      <text class="holder" x="21" y="96">Owen Latimer</text>
      <text class="phone" x="417" y="143" text-anchor="end">Phone Number:&#160; 040055501924</text>
      <text class="service" x="21" y="165">Commercial &amp; Domestic Painting</text>
      <text class="contact" x="21" y="212">Contact Us: KevinWalshCoatings@inbox.com.au</text>
    </svg>
  </article>

</main>
</body>
</html>
```